"When Grapes Remember" Book Cover Design

I need a design for the cover of a book I have written. I'm attaching the lead into the book to help provide context for you. I want the cover to be unique and outside of the box while still staying in line with the energy and feel of the content.

"Wine always had a way of speaking to me, even if I didn’t quite understand what it was saying. Upon making a decision to spend my life pursuing wine, I began to hear it loud and clear. I knew it had to be more than rich man’s drink, lifestyle trend, or just frivolous alcohol. I resolved it had a deeper meaning. In the years of trying to understand wine’s whole story, it ended up crafting mine.
When Grapes Remember is the intertwining of two personal stories, one about wine and one about myself. My goal is to tell wine’s story in tandem with my own. In this way, I can give wine the authentic voice it deserves. I want you to learn about wine like I learned, little by little. Each Wine 101 chapter seeks to answer the most common questions and misconceptions I have encountered with wine throughout the years. Every wine chapter will give you a foundation to build on, more confidence, and a greater love for wine."

Thank you for your time!

Target Market(s)

Men and Women Wine Lovers between the ages of 25-50

Colors

Designer to choose colors to be used in the design.

Requirements
Must have
• An eye catching appeal. Connect the title with the contents and convey the spirit of the book. A way to showcase the contents without being overly obvious and still having some mystery to the contents. Invite the potential reader to look deeper.

```html
<!DOCTYPE html>
<html lang="en">
<head>
<meta charset="utf-8">
<title>When Grapes Remember — Book Cover</title>
<link rel="stylesheet" href="https://fonts.googleapis.com/css2?family=Cinzel:wght@400&display=swap">
<style>
  :root {
    --page-bg: #f7f7f7;
    --cover-rose: #d3aaa7;
    --cover-rose-mid: #cba19e;
    --cover-rose-low: #9f6866;
    --title-wine: #7e0b0c;
    --glow-cream: #f3eeeb;
    --glow-sand: #dcc3ae;
    --wine-bright: #a8142f;
    --wine-deep: #3a0006;
  }
  * { margin: 0; padding: 0; box-sizing: border-box; }
  html, body {
    width: 1200px;
    height: 800px;
    overflow: hidden;
    background: var(--page-bg);
  }
  .canvas {
    width: 1200px;
    height: 800px;
    display: flex;
    align-items: center;
    justify-content: center;
  }
  .book-cover {
    position: relative;
    width: 470px;
    height: 740px;
    overflow: hidden;
    background:
      radial-gradient(ellipse 300px 260px at 330px 470px, var(--glow-cream) 0%, rgba(243,238,235,0.8) 45%, rgba(243,238,235,0) 100%),
      linear-gradient(180deg, var(--cover-rose) 0%, var(--cover-rose-mid) 42%, var(--glow-sand) 72%, var(--cover-rose-low) 100%);
  }
  .cover-art {
    position: absolute;
    left: 0;
    top: 330px;
    width: 470px;
    height: 410px;
    background: linear-gradient(150deg,
      rgba(243,238,235,0) 0%,
      rgba(243,238,235,0.6) 30%,
      var(--wine-bright) 55%,
      var(--wine-deep) 78%,
      rgba(120,40,45,0.6) 100%);
    -webkit-mask-image: radial-gradient(ellipse 240px 180px at 200px 220px, #000 35%, transparent 100%);
    mask-image: radial-gradient(ellipse 240px 180px at 200px 220px, #000 35%, transparent 100%);
  }
  .title {
    position: absolute;
    top: 88px;
    left: 0;
    right: 0;
    text-align: center;
    font-family: "Cinzel", serif;
    font-weight: 400;
    color: var(--title-wine);
    text-transform: uppercase;
    line-height: 1;
  }
  .title-line { display: block; }
  .title-line--upper {
    font-size: 54px;
    letter-spacing: 0.12em;
    padding-left: 0.12em;
    margin-bottom: 12px;
  }
  .title-line--main {
    font-size: 60px;
    letter-spacing: 0.04em;
    padding-left: 0.04em;
    margin-top: 8px;
  }
</style>
</head>
<body>
  <main class="canvas">
    <section class="book-cover">
      <div class="cover-art" role="img" aria-label="Photograph of a tilted wine glass holding red wine, a single drop falling into its surface"></div>
      <h1 class="title">
        <span class="title-line title-line--upper">When</span>
        <span class="title-line title-line--upper">Grapes</span>
        <span class="title-line title-line--main">Remember</span>
      </h1>
    </section>
  </main>
</body>
</html>
```